Wild Mo's Wine Label Project

We need a new entry level wine label called "Wild Mo's" for a range of wines we are developing from inland Australia. Our company is made up of three youngish guys who live hard and love taking the mickey. Wild Mo is Wild Moss - the largest and loudest of the three partners (and ideally this label will take the mickey out of him). We've grown the grapes ourselves for this first release which will be a 2012 Pinot Gris. Wine style is dry, young, fresh and contemporary and pitched at the sub AUD $10 retail price point. The package will be flint (clear) claret shape bottle with plain screwcap (colour matched to suit the winning label design).

I've attached a couple of photos of Wild Moss to give you some idea of his presence and persona.

Target Market(s)

Semi educated 25 - 40 year old wine drinkers. Skewed towards females.

Industry/Entity Type

Retail

Requirements
Should not have
• Anything traditional or old fashioned

```html
<!DOCTYPE html>
<html lang="en">
<head>
<meta charset="utf-8">
<title>Wild Mo's – Pinot Gris Label</title>
<link rel="stylesheet" href="https://fonts.googleapis.com/css2?family=Bebas+Neue&family=Josefin+Sans:wght@300&display=swap">
<style>
  :root {
    --paper: #ffffff;
    --band: #dfd157;
    --disc: #f5dc78;
    --ring: #f2d86a;
    --olive: #b1aa3f;
    --tagline: #f3a35a;
  }
  html, body {
    margin: 0;
    padding: 0;
    overflow: hidden;
    background: var(--paper);
  }
  .label {
    position: relative;
    width: 1200px;
    height: 927px;
    background: var(--paper);
    overflow: hidden;
  }
  .label__art {
    position: absolute;
    inset: 0;
    width: 1200px;
    height: 927px;
  }
  .band { fill: var(--band); }
  .disc { fill: var(--disc); }
  .disc-ring { fill: none; stroke: var(--ring); stroke-width: 2.5; }
  .tagline {
    font-family: "Josefin Sans", sans-serif;
    font-weight: 300;
    font-size: 31px;
    fill: var(--tagline);
  }
  .wine-name {
    font-family: "Bebas Neue", sans-serif;
    font-size: 172px;
    fill: var(--olive);
    letter-spacing: 2px;
  }
</style>
</head>
<body>
  <main class="label">
    <svg class="label__art" viewBox="0 0 1200 927" xmlns="http://www.w3.org/2000/svg">
      <defs>
        <path id="tagline-arc" d="M 341 470 A 260 260 0 0 1 861 470"/>
      </defs>

      <rect class="band" x="0" y="327" width="1200" height="272"/>

      <circle class="disc" cx="601" cy="464" r="278"/>
      <circle class="disc-ring" cx="601" cy="464" r="282"/>

      <text class="tagline" text-anchor="middle">
        <textPath href="#tagline-arc" startOffset="50%">dry, young, fresh</textPath>
      </text>

      <text class="wine-name" x="601" y="530" text-anchor="middle">Wild Mo</text>
    </svg>
  </main>
</body>
</html>
```